Cannabis Vape Cartridge Box. For HUGE Cannabis brand.

We need help with a product for our All-in-One Rosin Vape product. Our brand is called Corvin, and we are based in New Mexico. The product is all natural so we want the design look like natural as well. We will be using a soft touch box, so we want the packaging to look how the box feels in the hands. The box feels soft and smooth. We do not want to use any cannabis leaves in the design. We are also interested in vibrational patterns. I have attached examples of packaging that we like as well as the template of our boxes we will be using and also our logos.
Updates
With all new designs- please put the word Rosin on the box.
Colors
Designer to choose colors to be used in the design.
Look and feel

```html
<!DOCTYPE html>
<html lang="en">
<head>
<meta charset="utf-8">
<title>Corvin Rosin Disposable Vape – Box Dieline</title>
<link rel="stylesheet" href="https://fonts.googleapis.com/css2?family=Oswald:wght@500;600&family=Roboto+Condensed:wght@400;700&family=Mrs+Saint+Delafield&display=swap">
<style>
  :root {
    --page: #f9c7a6;
    --cream: #fbdac6;
    --ink: #1a1414;
    --fold: rgba(140, 40, 60, 0.35);
    --orange: #ef7a50;
    --red: #c2293d;
    --crimson: #8e1b3c;
    --plum: #4c1232;
    --alert: #e2282f;
    --light-text: #fbdac6;
  }
  html, body {
    margin: 0;
    width: 1200px;
    height: 900px;
    overflow: hidden;
    background: var(--page);
  }
  .stage {
    width: 1200px;
    height: 900px;
    display: flex;
    align-items: center;
    justify-content: center;
  }
  .dieline { width: 486px; height: 880px; display: block; }
  .panel-cream { fill: var(--cream); }
  .fold-line { fill: none; stroke: var(--fold); stroke-width: 2; }
  .info-card { fill: var(--cream); }
  .info-head { font-family: "Oswald", sans-serif; font-weight: 600; font-size: 19px; fill: var(--ink); }
  .info-body { font-family: "Roboto Condensed", sans-serif; font-size: 13.5px; fill: var(--ink); }
  .info-body .strong { font-weight: 700; }
  .brand-name { font-family: "Oswald", sans-serif; font-weight: 600; font-size: 52px; fill: var(--ink); letter-spacing: 2px; }
  .brand-dot { fill: var(--ink); }
  .tagline { font-family: "Oswald", sans-serif; font-weight: 500; font-size: 17px; fill: var(--light-text); letter-spacing: 0.5px; }
  .product-name { font-family: "Mrs Saint Delafield", cursive; font-size: 76px; fill: var(--light-text); }
  .weight { font-family: "Oswald", sans-serif; font-weight: 500; font-size: 16px; fill: var(--light-text); }
  .lid-name { font-family: "Oswald", sans-serif; font-weight: 600; font-size: 26px; fill: var(--ink); letter-spacing: 1px; }
  .thc-frame { fill: var(--cream); stroke: var(--alert); stroke-width: 5; }
  .thc-inner { fill: none; stroke: var(--alert); stroke-width: 3; }
  .thc-label { font-family: "Oswald", sans-serif; font-weight: 600; font-size: 24px; fill: var(--alert); }
</style>
</head>
<body>
<main class="stage">
  <svg class="dieline" viewBox="1260 60 840 1520" xmlns="http://www.w3.org/2000/svg" aria-label="Corvin Rosin disposable vape box, flat dieline">
    <defs>
      <linearGradient id="wave-tones" x1="0" y1="0" x2="0.35" y2="1">
        <stop offset="0" stop-color="var(--orange)"/>
        <stop offset="0.35" stop-color="var(--red)"/>
        <stop offset="0.62" stop-color="var(--crimson)"/>
        <stop offset="1" stop-color="var(--plum)"/>
      </linearGradient>
      <clipPath id="box-shape">
        <path d="M1283,365 L1420,345 L1420,1297 L1283,1277 Z"/>
        <rect x="1420" y="345" width="652" height="952"/>
        <path d="M1590,345 L1590,330 L1630,215 L1750,215 L1750,345 Z"/>
        <path d="M1750,345 L1750,180 L1757,180 C1757,120 1780,80 1830,80 C1880,80 1905,120 1905,180 L1913,180 L1913,345 Z"/>
        <path d="M1913,345 L1913,215 L2030,215 L2072,320 L2072,345 Z"/>
        <path d="M1420,1297 L1585,1297 L1585,1460 C1585,1510 1570,1557 1540,1557 L1465,1557 C1435,1557 1420,1510 1420,1460 Z"/>
        <path d="M1590,1297 L1745,1297 L1735,1425 L1605,1425 Z"/>
        <path d="M1920,1297 L2072,1297 L2072,1425 L1950,1425 Z"/>
      </clipPath>
    </defs>

    <g clip-path="url(#box-shape)">
      <rect class="panel-cream" x="1270" y="70" width="820" height="1500"/>
      <path role="img" aria-label="Layered flowing sand-dune wave pattern in orange, red and plum"
            fill="url(#wave-tones)"
            d="M1283,470 C1400,420 1450,650 1600,565 C1720,500 1760,770 1900,785 C1990,795 2040,900 2072,945 L2072,1600 L1283,1600 Z"/>
    </g>

    <g class="folds">
      <path class="fold-line" d="M1420,345 V1297 M1585,345 V1297 M1750,345 V1297 M1913,345 V1297"/>
      <path class="fold-line" d="M1420,345 H2072 M1420,1297 H2072 M1750,180 H1913 M1420,1460 H1585"/>
    </g>

    <g class="info-panel">
      <rect class="info-card" x="1427" y="345" width="151" height="945"/>
      <text class="info-head" x="1431" y="390">MUST BE 21+ TO ENJOY</text>
      <text class="info-body" x="1431">
        <tspan x="1431" y="411" class="strong">WARNING: For use by</tspan>
        <tspan x="1431" y="428"><tspan class="strong">adults 21 and over.</tspan> Keep</tspan>
        <tspan x="1431" y="445">out of reach of children.</tspan>
        <tspan x="1431" y="462">Do not drive or operate</tspan>
        <tspan x="1431" y="479">heavy machinery while</tspan>
        <tspan x="1431" y="496">under the influence of</tspan>
        <tspan x="1431" y="513">cannabis. BE CAUTIOUS a</tspan>
        <tspan x="1431" y="530" class="strong">Cannabinoid edibles can</tspan>
        <tspan x="1431" y="547" class="strong">take up to two hours or</tspan>
        <tspan x="1431" y="564"><tspan class="strong">more to take effect.</tspan> This</tspan>
        <tspan x="1431" y="581">product is not approved</tspan>
        <tspan x="1431" y="598">by the FDA to treat, cure,</tspan>
        <tspan x="1431" y="615">or prevent any disease.</tspan>
        <tspan x="1431" y="632">FDA has not evaluated</tspan>
        <tspan x="1431" y="649">this product for safety,</tspan>
        <tspan x="1431" y="666">effectiveness, and quality.</tspan>
        <tspan x="1431" y="683">There may be long term.</tspan>
        <tspan x="1431" y="700">adverse health effects</tspan>
        <tspan x="1431" y="717">from consumption of</tspan>
        <tspan x="1431" y="734">cannabis, including</tspan>
        <tspan x="1431" y="751">additional risks for</tspan>
        <tspan x="1431" y="768">women who are or may</tspan>
        <tspan x="1431" y="785">become pregnant or are</tspan>
        <tspan x="1431" y="802">breastfeeding. For</tspan>
        <tspan x="1431" y="819">accidental Ingestion: Call</tspan>
        <tspan x="1431" y="836">Poison Control</tspan>
        <tspan x="1431" y="853">1-800-555-0142</tspan>
        <tspan x="1431" y="886" class="strong">INGREDIENTS:</tspan>
        <tspan x="1431" y="903">Ethanol extracted</tspan>
        <tspan x="1431" y="920">Cannabis oil, natural</tspan>
        <tspan x="1431" y="937">terpenes</tspan>
        <tspan x="1431" y="965" class="strong">No pesticides used in the</tspan>
        <tspan x="1431" y="982" class="strong">making of this product.</tspan>
        <tspan x="1431" y="1011"><tspan class="strong">Solvents used:</tspan> Ethanol</tspan>
        <tspan x="1431" y="1163" class="strong">Expires one year after</tspan>
        <tspan x="1431" y="1180" class="strong">manufacturing date.</tspan>
        <tspan x="1431" y="1228"><tspan class="strong">Intended use:</tspan> Inhalant</tspan>
        <tspan x="1431" y="1256"><tspan class="strong">DIRECTIONS:</tspan> Press to lips</tspan>
        <tspan x="1431" y="1273">and inhale</tspan>
      </text>
    </g>

    <g class="lid">
      <text class="lid-name" x="1831" y="272" text-anchor="middle">CORVIN</text>
    </g>

    <g class="front-panel">
      <circle class="brand-dot" cx="1831" cy="470" r="14"/>
      <text class="brand-name" x="1831" y="560" text-anchor="middle">CORVIN</text>
      <text class="tagline" x="1831" y="1104" text-anchor="middle">CAREFULLY BLENDED</text>
      <text class="tagline" x="1831" y="1127" text-anchor="middle">DISPOSABLE VAPE</text>
      <text class="product-name" x="1831" y="1200" text-anchor="middle">Rosin</text>
      <text class="weight" x="1831" y="1252" text-anchor="middle">1 GRAM</text>
    </g>

    <g class="thc-mark" transform="translate(1993,1097)">
      <rect class="thc-frame" x="-44" y="-44" width="88" height="88" transform="rotate(45)"/>
      <rect class="thc-inner" x="-34" y="-34" width="68" height="68" transform="rotate(45)"/>
      <rect x="-3" y="-40" width="6" height="20" fill="var(--alert)"/>
      <circle cx="0" cy="-14" r="3.5" fill="var(--alert)"/>
      <text class="thc-label" x="0" y="10" text-anchor="middle">THC</text>
    </g>
  </svg>
</main>
</body>
</html>
```